Medical equipment business looking for professional, unique business card

We need a business card design for a durable medical equipment company. We are small but would like our cards to express that we are much bigger. We focus on braces (back, knee, wrist, etc) but also do crutches, rollators, wheelchairs- basically medical equipment that gets you going and back in Action. Our colors are blue and green and our logo has an arrow and use of a "spine". We'd like to express professionalism while being unique.

Industry/Entity Type

Medical Equipment

Contact Information for Business Card

Professional feel but unique. Memorable.

Font styles to use
Serif
Sans Serif
Other font styles liked:
• verdana

Requirements
Must have
• card holders cell#, business phone#, fax#, email, website address, business address, logo
Nice to have
• use of medical/healthcare related descriptive words, items, look
Should not have
• the wrong colors or cartoon characters.

```html
<!DOCTYPE html>
<html lang="en">
<head>
<meta charset="utf-8">
<title>Kinetra Medical – Business Card</title>
<link rel="stylesheet" href="https://fonts.googleapis.com/css2?family=Open+Sans:wght@400;600;700&display=swap">
<style>
  :root {
    --backdrop: #6e6e72;
    --card-white: #ffffff;
    --brand-navy: #08466b;
    --brand-green: #8cc43f;
    --text-light: #ffffff;
  }
  html, body {
    margin: 0;
    width: 1200px;
    height: 914px;
    overflow: hidden;
    background: var(--backdrop);
    font-family: "Open Sans", Verdana, sans-serif;
  }
  .card {
    position: absolute;
    left: 371px;
    top: 57px;
    width: 457px;
    height: 800px;
    background: var(--card-white);
    overflow: hidden;
    box-shadow: 0 10px 30px rgba(0,0,0,0.25);
  }
  .card-art {
    position: absolute;
    inset: 0;
    width: 100%;
    height: 100%;
  }
  .wordmark {
    position: absolute;
    top: 42px;
    right: 34px;
    display: flex;
    align-items: center;
    gap: 10px;
    color: var(--brand-navy);
    font-weight: 600;
    font-size: 30px;
    letter-spacing: 0.2px;
    white-space: nowrap;
  }
  .wordmark-dot {
    width: 14px;
    height: 14px;
    border-radius: 50%;
    background: var(--brand-green);
  }
  .contact {
    position: absolute;
    left: 56px;
    top: 470px;
    color: var(--text-light);
    letter-spacing: 0.6px;
    white-space: nowrap;
  }
  .contact-name {
    margin: 0;
    font-size: 26px;
    font-weight: 700;
    line-height: 1.1;
  }
  .contact-role {
    margin: 2px 0 18px;
    font-size: 16px;
  }
  .contact-address,
  .contact-lines {
    margin: 0 0 14px;
    font-size: 16px;
    line-height: 1.3;
    font-style: normal;
  }
</style>
</head>
<body>
  <section class="card">
    <svg class="card-art" viewBox="0 0 350 600" preserveAspectRatio="none" aria-hidden="true">
      <path class="navy-wave" fill="#08466b"
        d="M0,0 L22,0 C14,120 110,230 215,305 C300,365 330,470 312,600 L0,600 Z"/>
      <path class="green-swoosh" fill="#8cc43f"
        d="M48,18 C50,140 150,245 262,318 C335,370 350,470 332,585 C335,480 305,395 245,345 C145,262 38,160 48,18 Z"/>
    </svg>

    <div class="wordmark">
      <span class="wordmark-dot"></span>
      <span class="wordmark-name">Kinetra Medical</span>
    </div>

    <div class="contact">
      <p class="contact-name">Daniel Reeve</p>
      <p class="contact-role">Owner</p>
      <address class="contact-address">48 Harbor Lane<br>Ridgefield State<br>Northland</address>
      <p class="contact-lines">55 284 9130<br>www.kinetramedical.com<br>daniel@kinetramedical.com</p>
    </div>
  </section>
</body>
</html>
```